More Modern Look Required! Industry leading Property Management company needs a new website!

We are wanting to make our website more modern, as we find it is too cluttered, seems "old" and we want a new look. (www.tallowbrookrm.com)

We are wanting something fresh, clean and responsive, something that aligns with today's social media demands, something that allows our potential customers to immediately get a sense of the type of company we are.

Our current website was created on Wordpress and we will be keeping that core platform but wanting a new look and feel to it. The only thing we want to keep on the website is our "FOR RENT" page, although again we are open to having that look completely different as well (our programmers can adapt the functionality later)

Here is a synopsis of our branding statements:

CORE VALUES:
1. Passion
2. Innovation
3. Integrity (doing the right thing, even when it's difficult)
4. Empathy
5. Education

CORE FOCUS:
Our vision is to be the premier company for the delivery of all aspects of property management showing our passion for this industry, by innovating our service using cutting-edge technology, helping and educating investors to create aspirational and sustainable communities, adding value to their real estate assets, and working in partnership with all stakeholders including residents, showing empathy and integrity.

Brand Essence

When our customers experience our product or service, it brings forth an emotion of absolute trust that we have their best interests at heart

Brand Personality

We are a company that is passionate about our customers, our company and our vision to be leaders in the field of property management. We are visionaries that aren't afraid to use cutting edge technologies to improve our products and service.

Position or Value Proposition

To whom are we speaking?
- real estate investors, including first timers that are giving us their first starter home. They are not "big time" investors, and because they are giving us their first home (in contrast to an investor buying a rental property, often sight unseen) they are more emotionally tied to their property and will require a company that inspires trust and confidence.

What is our brand promise?
- we will do our best to serve our clients, both owners and tenants, to give them prompt communication, clear, concise answers to their questions, and look after their property quickly and competently.

Why is our product different than the competition and why should our customers care?
- Our management product is superior because we use a combination of technology and strict procedures to ensure each client's experience is consistent, each and every time.
Updates

Need extra days to review

Industry/Entity Type

Real Estate and Property Management

Number of Pages Required

5+ page

Requirements
Must have
• Must be compatible on Wordpress, our existing web platform. Please see our existing website at www.tallowbrookrm.com to familiarize yourself with our current site. Must incorporate For Rent section
Nice to have
• Built in reviews, contact us form, awards page including Fernleigh Patron Prizes (we just won again for Best Property Management Company, 8 years in a row)
Should not have
• Too many pages. Currently we feel there is too much information on each tab, and we can consolidate into about 5 or 6 tabs.

```html
<!DOCTYPE html>
<html lang="en">
<head>
<meta charset="utf-8">
<title>Tallowbrook Residential Management</title>
<link href="https://fonts.googleapis.com/css2?family=Jost:wght@400;500;600&family=Poppins:wght@500;600&display=swap" rel="stylesheet">
<style>
:root{
  --blue:#1589d2;
  --blue-soft:#cfe6f5;
  --navy:#1c2a5e;
  --ink:#1d2233;
  --text:#3a3f4d;
  --muted:#7d8290;
  --pale:#eef3f9;
  --line:#e3e7ee;
  --footer:#151a32;
  --star:#f4b400;
  --white:#fff;
}
*{box-sizing:border-box;margin:0;padding:0}
html,body{width:1200px;height:5226px;overflow:hidden}
body{font-family:"Jost",sans-serif;color:var(--text);background:var(--white);position:relative}
a{color:inherit;text-decoration:none}

/* header */
.site-header{position:absolute;top:0;left:0;width:1200px;height:100px;background:var(--white)}
.brand{position:absolute;left:98px;top:14px;display:flex;align-items:center;gap:12px}
.brand-mark{width:30px;height:30px;background:var(--blue)}
.brand-name{font-weight:600;font-size:26px;color:var(--navy);letter-spacing:1px}
.contact-strip{position:absolute;top:18px;left:535px;display:flex;gap:26px;align-items:center;font-size:12px;color:var(--ink)}
.contact-strip span{display:flex;align-items:center;gap:10px}
.ic-circle{width:24px;height:24px;border-radius:50%;background:#e9ecf1;display:inline-flex;align-items:center;justify-content:center}
.ticket-btn{position:absolute;left:874px;top:10px;width:228px;height:44px;background:var(--blue-soft);color:var(--blue);font-size:11px;font-weight:600;letter-spacing:.6px;display:flex;align-items:center;justify-content:center;text-transform:uppercase}
.main-nav{position:absolute;left:95px;top:69px;width:1008px;height:53px;background:var(--blue);display:flex;justify-content:space-around;align-items:center;z-index:2}
.main-nav a{color:var(--white);font-size:11.5px;font-weight:600;letter-spacing:.6px;text-transform:uppercase}

/* hero */
.hero{position:absolute;top:100px;left:0;width:1200px;height:566px;
  background:
    radial-gradient(ellipse 220px 260px at 880px 330px,rgba(190,200,210,.55),transparent 70%),
    radial-gradient(ellipse 300px 200px at 620px 160px,rgba(170,175,180,.5),transparent 70%),
    radial-gradient(ellipse 260px 220px at 160px 420px,rgba(120,90,60,.55),transparent 70%),
    linear-gradient(100deg,#4a4c58 0%,#6f6a66 30%,#8a8c92 55%,#7b8088 75%,#555b68 100%)}
.hero::after{content:"";position:absolute;inset:0;background:rgba(25,30,50,.32)}
.hero-inner{position:absolute;z-index:1;top:185px;left:0;width:1200px;text-align:center;color:var(--white)}
.hero h1{font-size:54px;font-weight:500;line-height:64px}
.hero p{font-size:14.5px;line-height:27px;margin-top:18px;font-weight:500}
.hero-actions{display:flex;justify-content:center;gap:26px;margin-top:24px}
.btn{height:42px;display:inline-flex;align-items:center;justify-content:center;font-size:11px;font-weight:600;letter-spacing:.8px;text-transform:uppercase}
.btn-light{width:188px;background:var(--white);color:var(--blue)}
.btn-blue{width:186px;background:var(--blue);color:var(--white)}

/* video */
.video-band{position:absolute;top:666px;left:0;width:1200px;height:558px;background:var(--pale)}
.video-title{position:absolute;top:738px;left:0;width:1200px;text-align:center;font-size:38px;font-weight:500;color:var(--ink);line-height:54px}
.video-frame{position:absolute;left:126px;top:885px;width:948px;height:502px;
  background:
    radial-gradient(ellipse 140px 200px at 480px 400px,rgba(120,60,50,.35),transparent 70%),
    radial-gradient(circle 60px at 860px 180px,rgba(250,220,90,.55),transparent 70%),
    linear-gradient(180deg,#e4e4e6 0%,#dedfe2 24%,#9fcde2 25%,#86bfd8 40%,#4f97bf 52%,#3f86b2 62%,#c9a667 68%,#d6b276 100%)}
.play{position:absolute;left:530px;top:1058px;width:130px;height:130px;border-radius:50%;background:rgba(255,255,255,.25);display:flex;align-items:center;justify-content:center}
.play-core{width:80px;height:80px;border-radius:50%;background:rgba(255,255,255,.35);display:flex;align-items:center;justify-content:center}

/* services */
.section-title{position:absolute;left:0;width:1200px;text-align:center;font-weight:500;color:var(--ink)}
.services-title{top:1480px;font-size:38px}
.services-lead{position:absolute;top:1548px;left:0;width:1200px;text-align:center;font-size:13.5px;line-height:24px;color:var(--ink);font-weight:500}
.service{position:absolute;width:240px;text-align:center}
.hex{width:84px;height:92px;margin:0 auto;background:var(--white);clip-path:polygon(50% 0,100% 25%,100% 75%,50% 100%,0 75%,0 25%);display:flex;align-items:center;justify-content:center;box-shadow:0 0 0 1px var(--line) inset}
.service h3{font-size:15px;font-weight:500;color:var(--ink);margin-top:20px}
.service p{font-size:12.5px;line-height:23px;color:var(--muted);margin-top:8px}

/* facts */
.facts-title{top:2205px;font-size:25px;font-family:"Poppins",sans-serif;font-weight:600}
.fact{position:absolute;top:2262px;width:213px;height:101px;background:var(--white);border:1px solid var(--line);box-shadow:0 4px 14px rgba(20,30,60,.07);text-align:center}
.fact .label{margin-top:18px;font-size:10px;letter-spacing:2px;color:var(--muted);display:flex;justify-content:center;gap:8px;align-items:center}
.fact .num{font-family:"Poppins",sans-serif;font-weight:600;font-size:44px;color:var(--ink);line-height:56px;margin-top:4px}

/* why */
.why-photo{position:absolute;top:2422px;left:0;width:1200px;height:556px;
  background:
    radial-gradient(ellipse 200px 180px at 420px 300px,rgba(190,80,60,.45),transparent 70%),
    radial-gradient(ellipse 180px 140px at 160px 420px,rgba(235,228,215,.8),transparent 70%),
    radial-gradient(ellipse 200px 300px at 900px 120px,rgba(255,230,170,.7),transparent 70%),
    linear-gradient(90deg,#9c8a73 0%,#b49b7c 25%,#d6b887 50%,#e8d8b5 65%,#cdd3da 85%,#aab3bf 100%)}
.why-card{position:absolute;left:601px;top:2532px;width:480px;height:495px;background:var(--blue);color:var(--white);padding:58px 38px 0}
.why-card h2{font-size:38px;font-weight:500;line-height:46px}
.why-card p{font-size:12.5px;line-height:24px;margin-top:30px}
.why-card p+p{margin-top:24px}

/* properties */
.props-bg{position:absolute;top:3020px;left:0;width:1200px;height:612px;background:linear-gradient(180deg,#fff 0%,#f4f6f9 30%,#eceff3 100%)}
.props-title{top:3098px;font-size:38px}
.tabs{position:absolute;top:3184px;left:0;width:1200px;display:flex;justify-content:center;gap:56px;font-size:14px;font-weight:500;color:var(--ink)}
.tabs .active{color:var(--blue)}
.map{position:absolute;top:3228px;left:0;width:1200px;height:404px;
  background:
    radial-gradient(ellipse 360px 150px at 600px 190px,rgba(140,185,215,.45),transparent 72%),
    radial-gradient(ellipse 260px 120px at 360px 150px,rgba(150,190,215,.3),transparent 70%),
    radial-gradient(ellipse 200px 110px at 880px 140px,rgba(150,190,215,.3),transparent 70%),
    radial-gradient(ellipse 700px 260px at 600px 200px,#e4e8ed 0%,#eaedf1 55%,#f1f3f6 100%)}

/* testimonials */
.reviews{position:absolute;top:3632px;left:0;width:1200px;height:520px;background:var(--navy)}
.reviews-title{position:absolute;top:3700px;left:0;width:1200px;text-align:center;color:var(--white);font-size:38px;font-weight:500}
.review{position:absolute;top:3786px;width:315px;height:292px;border:1px solid rgba(255,255,255,.12);padding:22px 22px 0}
.stars{color:var(--star);font-size:11px;letter-spacing:2px}
.review h4{color:var(--white);font-size:14.5px;font-weight:500;margin-top:10px}
.review p{color:#a9b0c8;font-size:11.5px;line-height:24px;margin-top:10px}
.reviewer{position:absolute;left:22px;top:218px;display:flex;align-items:center;gap:14px;color:var(--white);font-size:13px}
.reviewer small{display:block;color:#c7cbd9;font-size:10.5px}
.avatar{width:40px;height:40px;border-radius:50%;background:#c9a27f}
.arrow{position:absolute;top:3882px}

/* contact */
.contact-title{position:absolute;top:4228px;left:150px;font-size:38px;font-weight:500;color:var(--ink)}
.contact-lead{position:absolute;top:4290px;left:150px;width:520px;font-size:13px;line-height:24px;color:var(--muted)}
.field{position:absolute;height:46px;border:1px solid var(--line);font-size:11.5px;color:#a6abb6;padding:0 18px;display:flex;align-items:center}
.q-label{position:absolute;top:4494px;left:153px;font-size:12.5px;color:var(--ink)}
.radios{position:absolute;top:4528px;left:153px;display:flex;gap:26px;font-size:12px;color:var(--ink)}
.radios span{display:flex;align-items:center;gap:10px}
.dot{width:12px;height:12px;border-radius:50%;border:1px solid #b9bec8;display:inline-block}
.dot.on{border:4px solid var(--blue)}
.textarea{height:106px;align-items:flex-start;padding-top:20px}
.send{position:absolute;left:154px;top:4702px;width:175px;height:44px;background:var(--blue);color:var(--white);box-shadow:0 6px 14px rgba(21,137,210,.3)}
.info-head{position:absolute;left:761px;top:4354px;font-size:17px;line-height:26px;color:var(--ink);font-weight:500}
.info{position:absolute;left:761px;display:flex;gap:14px;font-size:11.5px;color:var(--muted);line-height:20px}
.info b{display:block;font-size:11px;letter-spacing:1px;color:var(--ink);font-weight:600}

/* footer */
.site-footer{position:absolute;top:4800px;left:0;width:1200px;height:426px;background:var(--footer);clip-path:polygon(0 64px,868px 0,1200px 42px,1200px 100%,0 100%);color:#c4c8d6}
.f-brand{position:absolute;left:152px;top:124px;display:flex;align-items:center;gap:12px}
.f-brand .brand-name{color:var(--white);font-size:24px}
.f-text{position:absolute;font-size:11.5px;line-height:22px;color:#dfe2ea}
.f-line{position:absolute;left:158px;display:flex;align-items:center;gap:16px;font-size:11.5px;color:#dfe2ea}
.f-col{position:absolute;top:126px}
.f-col h5{font-size:12px;color:var(--white);font-weight:500;margin-bottom:18px}
.f-col li{list-style:none;font-size:11.5px;line-height:27px;color:#aeb3c4}
.news li{line-height:16px;margin-bottom:18px}
.news small{display:block;font-size:9px;color:#6d7390}
.copyright{position:absolute;left:152px;top:396px;font-size:10.5px;color:#dfe2ea}
.copyright span{color:var(--blue)}
.social{position:absolute;left:905px;top:388px;display:flex;gap:14px}
.social i{width:24px;height:24px;border-radius:50%;background:#2a3052;display:block}
</style>
</head>
<body>

<header class="site-header">
  <div class="brand"><span class="brand-mark"></span><span class="brand-name">TALLOWBROOK</span></div>
  <div class="contact-strip">
    <span><i class="ic-circle"><svg width="11" height="11" viewBox="0 0 24 24"><path d="M6.6 10.8a15 15 0 006.6 6.6l2.2-2.2c.3-.3.7-.4 1-.2 1.1.4 2.3.6 3.6.6.6 0 1 .4 1 1V20c0 .6-.4 1-1 1A17 17 0 013 4c0-.6.4-1 1-1h3.5c.6 0 1 .4 1 1 0 1.3.2 2.5.6 3.6.1.3 0 .7-.2 1z" fill="#555"/></svg></i>204-555-0142</span>
    <span><i class="ic-circle"><svg width="11" height="11" viewBox="0 0 24 24"><path d="M6.6 10.8a15 15 0 006.6 6.6l2.2-2.2c.3-.3.7-.4 1-.2 1.1.4 2.3.6 3.6.6.6 0 1 .4 1 1V20c0 .6-.4 1-1 1A17 17 0 013 4c0-.6.4-1 1-1h3.5c.6 0 1 .4 1 1 0 1.3.2 2.5.6 3.6.1.3 0 .7-.2 1z" fill="#555"/></svg></i>Toll Free: 1-844-555-0190</span>
  </div>
  <a class="ticket-btn">Create maintenance ticket</a>
</header>
<nav class="main-nav">
  <a>Home</a><a>Services</a><a>Pricing</a><a>Home Watch</a><a>Leasing only</a><a>Rentals</a><a>FAQ</a><a>About us</a><a>Contact us</a>
</nav>

<section class="hero" role="img" aria-label="Photo of a couple viewing a bright kitchen with a property agent">
  <div class="hero-inner">
    <h1>Industry leading Property<br>Management solutions</h1>
    <p>Tallowbrook Residential Management in Winnipeg offers some of the most<br>premium services available for investors and tenants.</p>
    <div class="hero-actions"><a class="btn btn-light">Find your next home</a><a class="btn btn-blue">About our services</a></div>
  </div>
</section>

<section class="video-band"></section>
<h2 class="video-title">Is managing a property easy?Watch the<br>video to find out!</h2>
<div class="video-frame" role="img" aria-label="Animated video still of a relaxed landlord on a sunny beach with a caption about just collecting the rent"></div>
<div class="play"><div class="play-core"><svg width="26" height="30" viewBox="0 0 26 30"><path d="M2 2l22 13L2 28z" fill="#fff"/></svg></div></div>

<h2 class="section-title services-title">Services we provide</h2>
<p class="services-lead">Tallowbrook Residential Management in Winnipeg offers some of the most premium<br>services available for investors and tenants.</p>

<div class="service" style="left:174px;top:1630px">
  <div class="hex"><svg width="40" height="40" viewBox="0 0 40 40" fill="none" stroke="#3d6fb6" stroke-width="1.6"><path d="M6 20L20 8l14 12M10 17v16h20V17M16 33v-9h8v9"/></svg></div>
  <h3>Property Management</h3>
  <p>Using the latest technology and specially trained staff, we efficiently manage your property.</p>
</div>
<div class="service" style="left:476px;top:1630px">
  <div class="hex"><svg width="40" height="40" viewBox="0 0 40 40" fill="none" stroke="#3d6fb6" stroke-width="1.6"><rect x="9" y="8" width="22" height="26" rx="2"/><path d="M14 15h12M14 21h12M14 27h7"/></svg></div>
  <h3>Leasing and Renewals</h3>
  <p>We perform a comprehensive rental market evaluation to maximize your investment.</p>
</div>
<div class="service" style="left:775px;top:1630px">
  <div class="hex"><svg width="40" height="40" viewBox="0 0 40 40" fill="none" stroke="#3d6fb6" stroke-width="1.8"><path d="M10 30l14-14M26 10a5 5 0 106 6l-4 1-3-3zM12 10l18 20M10 12l4-4"/></svg></div>
  <h3>Property Maintenance</h3>
  <p>You'll never have to worry about that midnight call or have to scramble to find a plumber.</p>
</div>
<div class="service" style="left:326px;top:1880px">
  <div class="hex"><svg width="40" height="40" viewBox="0 0 40 40" fill="none" stroke="#3d6fb6" stroke-width="1.6"><path d="M8 32h24M8 32V10h16v22M28 12l4 4-12 12h-4v-4z"/></svg></div>
  <h3>Rehab and Construction</h3>
  <p>We provide maintenance and repair services, and can also help you with larger construction projects.</p>
</div>
<div class="service" style="left:630px;top:1880px">
  <div class="hex"><svg width="40" height="40" viewBox="0 0 40 40" fill="none" stroke="#3d6fb6" stroke-width="1.6"><rect x="9" y="9" width="22" height="24" rx="2"/><path d="M14 6v6M26 6v6M14 18h12M14 23h12M14 28h8"/></svg></div>
  <h3>Free Stuff</h3>
  <p>At Tallowbrook we want to help smaller landlords. We believe in "giving back" which is why we volunteer hundreds of hours per year.</p>
</div>

<h2 class="section-title facts-title">Facts overview</h2>
<div class="fact" style="left:254px"><div class="label"><svg width="12" height="12" viewBox="0 0 24 24"><path d="M3 11l9-8 9 8v10H3z" fill="#3d4fb6"/></svg>PROPERTIES</div><div class="num">447</div></div>
<div class="fact" style="left:495px"><div class="label"><svg width="12" height="12" viewBox="0 0 24 24"><rect x="4" y="4" width="16" height="18" fill="#e04848"/></svg>UNITS</div><div class="num">543</div></div>
<div class="fact" style="left:735px"><div class="label"><svg width="12" height="12" viewBox="0 0 24 24"><circle cx="12" cy="12" r="9" fill="#3bb56b"/></svg>INVESTORS</div><div class="num">317</div></div>

<div class="why-photo" role="img" aria-label="Photo of a smiling couple relaxing on a sofa in a sunlit living room"></div>
<div class="why-card">
  <h2>Why choose us as your property management company</h2>
  <p>Tallowbrook Residential Management has been recognized and voted multiple times as The Best Winnipeg Property Management Company by Fernleigh Patron Prizes. We are intently focussed on serving both owners and tenants and are dedicated to a culture of superior customer service.</p>
  <p>Whether you own one investment property or ten, the partnership process with Tallowbrook Residential Management is easy, efficient and rewarding.</p>
</div>

<div class="props-bg"></div>
<h2 class="section-title props-title">Properties Managed by Tallowbrook</h2>
<div class="tabs"><span class="active">All Properties</span><span>Available Properties</span></div>
<div class="map" role="img" aria-label="City map of Winnipeg with markers showing managed properties"></div>

<section class="reviews"></section>
<h2 class="reviews-title">What our customer says</h2>
<svg class="arrow" style="left:64px" width="28" height="14" viewBox="0 0 28 14"><path d="M27 7H2M8 1L2 7l6 6" stroke="#4a5790" stroke-width="1.5" fill="none"/></svg>
<svg class="arrow" style="left:1124px" width="28" height="14" viewBox="0 0 28 14"><path d="M1 7h25M20 1l6 6-6 6" stroke="#fff" stroke-width="1.5" fill="none"/></svg>
<article class="review" style="left:116px">
  <div class="stars">★★★★★</div>
  <h4>"Excited to have such quality..."</h4>
  <p>"Had a bathroom renovation completed by one of their contractors Rowan, he was very thorough in his work and communication about the work being done and to be completed..."</p>
  <div class="reviewer"><span class="avatar"></span><div>Maren Holt<small>Kansas City, Missouri</small></div></div>
</article>
<article class="review" style="left:455px">
  <div class="stars">★★★★★</div>
  <h4>"Highly recommended..."</h4>
  <p>"Elias is an extremely kind and professional person. He and his team have been on the lookout in each of the stages of the service. I highly recommend this great firm..."</p>
  <div class="reviewer"><span class="avatar" style="background:#b08c6c"></span><div>Devon Price<small>Kansas City, Missouri</small></div></div>
</article>
<article class="review" style="left:792px">
  <div class="stars">★★★★★</div>
  <h4>"It is exactly what I wanted..."</h4>
  <p>"Awesome company to work with. They are accommodating and will always try to help you as best as they can. I recommend working with Tallowbrook Residential ..."</p>
  <div class="reviewer"><span class="avatar" style="background:#a77b5c"></span><div>Aled Brooks<small>Kansas City, Missouri</small></div></div>
</article>

<h2 class="contact-title">Get in touch</h2>
<p class="contact-lead">We like to hear from you. Drop us a line below, ours sales expert will contact with you with in next 24 hoours.</p>
<div class="field" style="left:154px;top:4360px;width:254px">Full name</div>
<div class="field" style="left:428px;top:4360px;width:258px">Company name</div>
<div class="field" style="left:154px;top:4430px;width:254px">Email address</div>
<div class="field" style="left:428px;top:4430px;width:258px">Phone number</div>
<div class="q-label">What are you?</div>
<div class="radios">
  <span><i class="dot on"></i>I am an owner</span><span><i class="dot"></i>I am a renter</span><span><i class="dot"></i>I am a contractor</span><span><i class="dot"></i>Others</span>
</div>
<div class="field textarea" style="left:154px;top:4572px;width:532px">Tell us about your sales inquiry...</div>
<a class="btn send">Send message</a>

<div class="info-head">Don't hesitate to contact<br>us for any information.</div>
<div class="info" style="top:4428px"><svg width="12" height="12" viewBox="0 0 24 24"><path d="M2 5h20v14H2zM2 5l10 8 10-8" fill="#5b6070" stroke="#fff"/></svg><div><b>EMAIL</b>hello@tallowbrookrm.com</div></div>
<div class="info" style="top:4484px"><svg width="12" height="12" viewBox="0 0 24 24"><path d="M6.6 10.8a15 15 0 006.6 6.6l2.2-2.2c.3-.3.7-.4 1-.2 1.1.4 2.3.6 3.6.6.6 0 1 .4 1 1V20c0 .6-.4 1-1 1A17 17 0 013 4c0-.6.4-1 1-1h3.5c.6 0 1 .4 1 1 0 1.3.2 2.5.6 3.6.1.3 0 .7-.2 1z" fill="#5b6070"/></svg><div><b>PHONE</b>204-555-0142</div></div>
<div class="info" style="top:4540px"><svg width="12" height="12" viewBox="0 0 24 24"><path d="M12 2a7 7 0 00-7 7c0 5 7 13 7 13s7-8 7-13a7 7 0 00-7-7zm0 9.5A2.5 2.5 0 1112 6a2.5 2.5 0 010 5.5z" fill="#5b6070"/></svg><div><b>ADDRESS</b>220-1475 Corydon Ave<br>Winnipeg, MB R3M 0Y1</div></div>

<footer class="site-footer">
  <div class="f-brand"><span class="brand-mark"></span><span class="brand-name">TALLOWBROOK</span></div>
  <div class="f-text" style="left:152px;top:188px">220-1475 Corydon Ave<br>Winnipeg, MB R3M 0Y1</div>
  <div class="f-line" style="top:252px"><svg width="12" height="12" viewBox="0 0 24 24"><path d="M2 5h20v14H2z" fill="#fff"/></svg>204.555.0177</div>
  <div class="f-line" style="top:284px"><svg width="12" height="12" viewBox="0 0 24 24"><path d="M6.6 10.8a15 15 0 006.6 6.6l2.2-2.2c.3-.3.7-.4 1-.2 1.1.4 2.3.6 3.6.6.6 0 1 .4 1 1V20c0 .6-.4 1-1 1A17 17 0 013 4c0-.6.4-1 1-1h3.5c.6 0 1 .4 1 1 0 1.3.2 2.5.6 3.6.1.3 0 .7-.2 1z" fill="#fff"/></svg>office@tallowbrookrm.com</div>
  <div class="f-col" style="left:457px"><h5>Company</h5><ul><li>Services</li><li>Pricing</li><li>Home watch</li><li>Leasing only</li><li>Rental</li><li>FAQ</li><li>About us</li></ul></div>
  <div class="f-col news" style="left:641px"><h5>Latest news</h5><ul><li>› In non faucibus lorem non laoreet<small>06 Jan, 2020</small></li><li>› Nunc rhoncus iaculis pellent<small>06 Jan, 2020</small></li><li>› Ullam corper dolor mattis ac<small>06 Jan, 2020</small></li></ul></div>
  <div class="f-col" style="left:913px"><h5>Support</h5><ul><li>Terms and conditions</li><li>Privacy policy</li><li>Help</li><li>Contact us</li></ul></div>
  <div class="copyright">Copyright © 2023 <span>Tallowbrook</span> . All rights reserved</div>
  <div class="social"><i></i><i></i><i></i><i></i></div>
</footer>

</body>
</html>
```